emerald card

Belvardi/Gems
Est.1972
We are a direct Importer of Colombian Emeralds, with gem lab certificates KSR,PMB 1.0ct. and over.Gem ID and Country of origin
Hal Belvardi belvo@postwing.example
469 555 0176 www. belvardiline.example
The current web page is being redesigned,please ,Belvardi/Gems is a new company. We specialize in Colombian Emeralds.
Some of the designers used the existing web page and companies and created business cards for the wrong companies.
The blue back ground deign from Sri Lanka is the only card design that has all the correct information.

Target Market(s)

Fine Jewelry

Industry/Entity Type

Business

Contact Information for Business Card

Belvardi/Gems

Font styles to use
Other font styles liked:
• Roman

Requirements
Must have
• Belvardi/Gems Hal Belvardi
P.O.Box 318270 Dallas,Tx.75908 Ph. 469 555 0176 E-Mail:belvo@postwing.example
www.belvardiline.example, Emeralds over 1.0ct. are certified for Country of origin and Gem ID-KSR or PMB cerificates.

We are importers of Colombian Emeralds all Emeralds over 1.0ct.
Dallas,Tx. 75908
KSR,PMB
Nice to have
• Picture of Emerald
Should not have
• No other company names
We are changing information on our web site.do not use the web page for design.

```html
<!DOCTYPE html>
<html lang="en">
<head>
<meta charset="utf-8">
<title>Hal Belvardi – Emerald Business Card</title>
<link rel="stylesheet" href="https://fonts.googleapis.com/css2?family=Cinzel:wght@400&family=Tinos:wght@400;700&family=Arimo:wght@400;700&display=swap">
<style>
  :root {
    --page-bg: #e4e4e4;
    --card-bg: #ffffff;
    --card-edge: #d2d2d2;
    --green-main: #137a38;
    --green-soft: #3c9c5c;
    --green-deep: #0b5a2a;
    --emerald-dark: #064d24;
    --emerald-mid: #0f8a45;
    --emerald-light: #2fb86a;
    --mint-light: #d3f1e2;
    --mint-mid: #a8dcc2;
  }
  * { margin: 0; padding: 0; box-sizing: border-box; }
  html, body {
    width: 992px; height: 1200px; overflow: hidden;
    background: var(--page-bg);
  }
  .sheet { position: relative; width: 992px; height: 1200px; }

  .card {
    position: absolute; left: 75px; width: 870px; height: 495px;
    background: var(--card-bg);
    border: 1px solid var(--card-edge);
    border-radius: 26px;
    overflow: hidden;
  }
  .card--front { top: 68px; }
  .card--back { top: 627px; }

  .gem-photo { position: absolute; }
  .gem-photo--small {
    left: 137px; top: 28px; width: 193px; height: 160px;
    background: radial-gradient(circle at 50% 50%, var(--emerald-light) 0%, var(--emerald-mid) 45%, var(--emerald-dark) 100%);
    clip-path: polygon(8% 0, 92% 0, 100% 10%, 100% 90%, 92% 100%, 8% 100%, 0 90%, 0 10%);
  }
  .gem-photo--large {
    left: 47px; top: 41px; width: 408px; height: 417px;
    background: radial-gradient(circle at 50% 50%, var(--mint-light) 0%, var(--mint-mid) 100%);
    clip-path: polygon(12% 0, 88% 0, 100% 10%, 100% 90%, 88% 100%, 12% 100%, 0 90%, 0 10%);
  }

  .name-caps {
    position: absolute; left: 342px; top: 90px;
    font-family: "Cinzel", serif; font-weight: 400; font-size: 33px; letter-spacing: 1px;
    color: var(--green-main);
  }

  .contact-list { position: absolute; left: 174px; top: 240px; list-style: none; }
  .contact-item {
    display: flex; align-items: center; height: 44px;
    font-family: "Cinzel", serif; color: var(--green-main);
  }
  .contact-item svg { width: 22px; height: 22px; margin-right: 59px; fill: var(--green-main); }
  .contact-item--phone { font-size: 27px; }
  .contact-item--mail, .contact-item--web { font-size: 24px; letter-spacing: 1px; }
  .contact-item .globe { fill: none; stroke: var(--green-main); stroke-width: 1.6; }

  .gem-fields { position: absolute; left: 175px; top: 382px; }
  .gem-field {
    font-family: "Cinzel", serif; font-weight: 400; font-size: 26px; color: var(--green-soft);
    line-height: 43px; white-space: nowrap;
  }
  .gem-field .dots { font-family: "Tinos", serif; font-weight: 400; font-size: 20px; letter-spacing: 0.5px; }

  .name-bold {
    position: absolute; left: 493px; top: 226px;
    font-family: "Tinos", serif; font-weight: 700; font-size: 44px;
    color: var(--green-deep);
  }
  .company-details {
    position: absolute; left: 493px; top: 300px; width: 360px;
    font-family: "Arimo", sans-serif; font-size: 16px; line-height: 24px;
    color: var(--green-deep);
  }
  .company-details .company-name { font-weight: 700; }
  .site-plain {
    position: absolute; left: 493px; top: 431px;
    font-family: "Arimo", sans-serif; font-size: 25px;
    color: var(--green-deep);
  }
</style>
</head>
<body>
<main class="sheet">
  <section class="card card--front">
    <div class="gem-photo gem-photo--small" role="img" aria-label="Photo of a cut square emerald"></div>
    <h1 class="name-caps">Hal Belvardi</h1>
    <ul class="contact-list">
      <li class="contact-item contact-item--phone">
        <svg viewBox="0 0 24 24" aria-hidden="true"><path d="M2 9c2-4 18-4 20 0l-1 3-4-1v-2H7v2l-4 1zM6 13h12l2 7H4z"/></svg>
        469 555 0176
      </li>
      <li class="contact-item contact-item--mail">
        <svg viewBox="0 0 24 24" aria-hidden="true"><path d="M2 6h20v12H2zM4 8v1l8 5 8-5V8l-8 5z"/></svg>
        BELVO@POSTWING.EXAMPLE
      </li>
      <li class="contact-item contact-item--web">
        <svg viewBox="0 0 24 24" aria-hidden="true" class="globe"><circle cx="12" cy="12" r="9"/><ellipse cx="12" cy="12" rx="4" ry="9"/><path d="M3 12h18M5 7h14M5 17h14"/></svg>
        BELVARDILINE.EXAMPLE
      </li>
    </ul>
    <div class="gem-fields">
      <p class="gem-field">Gem ID : <span class="dots">.............................................................</span></p>
      <p class="gem-field">Coutry of origin : <span class="dots">.......................................</span></p>
    </div>
  </section>

  <section class="card card--back">
    <div class="gem-photo gem-photo--large" role="img" aria-label="Faint large photo of a cut square emerald"></div>
    <h2 class="name-bold">Hal Belvardi</h2>
    <div class="company-details">
      <p class="company-name">Belvardi/Gems · Est. 1972</p>
      <p>P.O.Box 318270 Dallas, Tx. 75908</p>
      <p>Importers of Colombian Emeralds</p>
      <p>Over 1.0ct. certified KSR, PMB</p>
    </div>
    <p class="site-plain">belvardiline.example</p>
  </section>
</main>
</body>
</html>
```